Brinmoor Suites internet banner add

Seldovia Alaska -I need a fabulous UNIQUE web banner for our two locations Brinmoor Suites Harbor Location and Brinmoor Suites Central location
All suites have full Kitchens
Open year Round
We cater to vacationers - fishermen - hikers - and families
Classy upbeat modern design
The dimensions for the banner ads are:

300x250
OR
728x90

Target Market(s)

Alaska- Nautical

Industry/Entity Type

Vacation rentals

Requirements
Must have
• I would like the attached photo as background Brinmoor Suites - always follow the quiet shore with our phone number- email - and 2 websites

```html
<!DOCTYPE html>
<html lang="en">
<head>
<meta charset="utf-8">
<title>Brinmoor Suites web banners</title>
<link href="https://fonts.googleapis.com/css2?family=Kaushan+Script&family=Courgette&family=Kalam:wght@400&family=Oswald:wght@600&family=Roboto:wght@500;700&display=swap" rel="stylesheet">
<style>
  :root {
    --board: #3a413e;
    --sky-top: #4f8fd0;
    --sky-low: #a9cbe8;
    --water: #3a6f9e;
    --forest: #2f4a2c;
    --forest-deep: #1f3120;
    --navy: #2b3f5c;
    --ink: #1d2a3c;
    --gold: #f6c73c;
    --white: #ffffff;
    --mist: rgba(235, 243, 250, 0.92);
  }
  html, body {
    margin: 0;
    padding: 0;
    width: 1200px;
    height: 960px;
    overflow: hidden;
    background: var(--board);
  }
  .canvas {
    position: relative;
    width: 1200px;
    height: 960px;
    background: radial-gradient(ellipse at center, #414945 0%, var(--board) 75%);
  }
  .ad {
    position: absolute;
    overflow: hidden;
    box-shadow: 0 2px 6px rgba(0,0,0,0.35);
  }
  .ad > div { white-space: nowrap; }
  .scenery {
    position: absolute;
    inset: 0;
    background: linear-gradient(180deg,
      var(--sky-top) 0%,
      var(--sky-low) 45%,
      var(--water) 58%,
      #4f6f52 66%,
      var(--forest) 80%,
      var(--forest-deep) 100%);
  }
  .leaderboard .scenery {
    background: linear-gradient(180deg,
      var(--sky-low) 0%,
      #c9dced 30%,
      var(--water) 55%,
      var(--forest) 85%,
      var(--forest-deep) 100%);
  }
  .leaderboard .logo-veil {
    position: absolute;
    left: 0; top: 0; bottom: 0;
    width: 300px;
    background: linear-gradient(90deg, var(--mist) 0%, var(--mist) 75%, rgba(235,243,250,0) 100%);
  }

  /* 300x250 rectangles */
  .rectangle { top: 84px; width: 360px; height: 300px; }
  .rectangle.one { left: 48px; }
  .rectangle.two { left: 420px; }
  .rectangle.three { left: 792px; }
  .rectangle .brand-name {
    position: absolute;
    left: 0; right: 0; top: 72px;
    text-align: center;
    font-family: "Roboto", sans-serif;
    font-weight: 700;
    font-size: 27px;
    line-height: 34px;
    letter-spacing: 2px;
    color: var(--navy);
    text-transform: uppercase;
  }
  .rectangle .tagline {
    position: absolute;
    left: 0; right: 0; top: 124px;
    text-align: center;
    color: var(--ink);
    font-size: 24px;
    line-height: 34px;
  }
  .rectangle .phone {
    position: absolute;
    left: 0; right: 0; top: 162px;
    text-align: center;
    font-family: "Oswald", sans-serif;
    font-weight: 600;
    font-size: 40px;
    line-height: 56px;
    color: var(--gold);
    text-shadow: 2px 2px 2px rgba(0,0,0,0.6);
  }
  .rectangle .contacts {
    position: absolute;
    left: 0; right: 0; top: 226px;
    text-align: center;
    font-family: "Roboto", sans-serif;
    font-weight: 500;
    font-size: 15px;
    line-height: 22px;
    color: var(--white);
    text-shadow: 1px 1px 2px rgba(0,0,0,0.7);
  }

  /* 728x90 leaderboards */
  .leaderboard { left: 163px; width: 874px; height: 108px; }
  .leaderboard.one { top: 455px; }
  .leaderboard.two { top: 606px; }
  .leaderboard.three { top: 762px; }
  .leaderboard .brand-name {
    position: absolute;
    left: 16px; top: 36px;
    width: 270px;
    text-align: center;
    font-family: "Roboto", sans-serif;
    font-weight: 700;
    font-size: 26px;
    line-height: 34px;
    letter-spacing: 2px;
    color: var(--navy);
    text-transform: uppercase;
  }
  .leaderboard .tagline {
    position: absolute;
    left: 338px; top: 6px;
    color: var(--ink);
    font-size: 24px;
    line-height: 32px;
  }
  .leaderboard .phone {
    position: absolute;
    left: 338px; top: 38px;
    font-family: "Oswald", sans-serif;
    font-weight: 600;
    font-size: 46px;
    line-height: 60px;
    color: var(--gold);
    text-shadow: 2px 2px 2px rgba(0,0,0,0.6);
  }
  .leaderboard .contacts {
    position: absolute;
    right: 26px; top: 44px;
    text-align: right;
    font-family: "Roboto", sans-serif;
    font-weight: 700;
    font-size: 13.5px;
    line-height: 18px;
    color: var(--white);
    text-shadow: 1px 1px 2px rgba(0,0,0,0.7);
  }
  .leaderboard.two .tagline, .leaderboard.three .tagline { top: 10px; font-size: 22px; }

  .script-brush { font-family: "Kaushan Script", cursive; }
  .script-round { font-family: "Courgette", cursive; }
  .script-light { font-family: "Kalam", cursive; }
</style>
</head>
<body>
<main class="canvas">

  <section class="ad rectangle one">
    <div class="scenery" role="img" aria-label="Photo of an Alaskan bay with snowy mountain and evergreen forest"></div>
    <div class="brand-name">Brinmoor Suites</div>
    <div class="tagline script-brush">Always follow the quiet shore</div>
    <div class="phone">907-555-0142</div>
    <div class="contacts">Brinmoor_Suites@mailbox.com<br>CentralSuitesofBrinmoor.com<br>BrinmoorHarborInn.com</div>
  </section>

  <section class="ad rectangle two">
    <div class="scenery" role="img" aria-label="Photo of an Alaskan bay with snowy mountain and evergreen forest"></div>
    <div class="brand-name">Brinmoor Suites</div>
    <div class="tagline script-round">Always follow the quiet shore</div>
    <div class="phone">907-555-0142</div>
    <div class="contacts">Brinmoor_Suites@mailbox.com<br>CentralSuitesofBrinmoor.com<br>BrinmoorHarborInn.com</div>
  </section>

  <section class="ad rectangle three">
    <div class="scenery" role="img" aria-label="Photo of an Alaskan bay with snowy mountain and evergreen forest"></div>
    <div class="brand-name">Brinmoor Suites</div>
    <div class="tagline script-light">Always follow the quiet shore</div>
    <div class="phone">907-555-0142</div>
    <div class="contacts">Brinmoor_Suites@mailbox.com<br>CentralSuitesofBrinmoor.com<br>BrinmoorHarborInn.com</div>
  </section>

  <section class="ad leaderboard one">
    <div class="scenery" role="img" aria-label="Wide photo of Alaskan coastline with distant snowy peak and forest"></div>
    <div class="logo-veil"></div>
    <div class="brand-name">Brinmoor Suites</div>
    <div class="tagline script-brush">Always follow the quiet shore</div>
    <div class="phone">907-555-0142</div>
    <div class="contacts">Brinmoor_Suites@mailbox.com<br>CentralSuitesofBrinmoor.com<br>BrinmoorHarborInn.com</div>
  </section>

  <section class="ad leaderboard two">
    <div class="scenery" role="img" aria-label="Wide photo of Alaskan coastline with distant snowy peak and forest"></div>
    <div class="logo-veil"></div>
    <div class="brand-name">Brinmoor Suites</div>
    <div class="tagline script-round">Always follow the quiet shore</div>
    <div class="phone">907-555-0142</div>
    <div class="contacts">Brinmoor_Suites@mailbox.com<br>CentralSuitesofBrinmoor.com<br>BrinmoorHarborInn.com</div>
  </section>

  <section class="ad leaderboard three">
    <div class="scenery" role="img" aria-label="Wide photo of Alaskan coastline with distant snowy peak and forest"></div>
    <div class="logo-veil"></div>
    <div class="brand-name">Brinmoor Suites</div>
    <div class="tagline script-light">Always follow the quiet shore</div>
    <div class="phone">907-555-0142</div>
    <div class="contacts">Brinmoor_Suites@mailbox.com<br>CentralSuitesofBrinmoor.com<br>BrinmoorHarborInn.com</div>
  </section>

</main>
</body>
</html>
```